Financial firm simple design

Classic business card design for a financial fund. 2 sided card- white on both sides.. One with just the company name centered and the other w the info. info included on that is :

Name
Company position
phone number
fax
email
website

Financial

```html
<!DOCTYPE html>
<html lang="en">
<head>
<meta charset="utf-8">
<title>Norvale Capital – Business Card</title>
<link href="https://fonts.googleapis.com/css2?family=Ubuntu:wght@400;500&display=swap" rel="stylesheet">
<style>
  :root {
    --backdrop: #e4e5e8;
    --card-white: #ffffff;
    --card-navy: #12295a;
    --card-navy-deep: #0c1c40;
    --ink-navy: #0f2f66;
    --ink-dark: #222428;
    --rule: #2a2a2a;
    --brand-light: #f2f3f6;
  }
  html, body {
    margin: 0;
    padding: 0;
    width: 1200px;
    height: 960px;
    overflow: hidden;
    background: var(--backdrop);
  }
  .canvas {
    width: 1200px;
    height: 960px;
    display: flex;
    flex-direction: column;
    align-items: center;
    justify-content: center;
    gap: 60px;
  }
  .card {
    width: 700px;
    height: 400px;
    position: relative;
    box-shadow: 0 10px 30px rgba(0,0,0,0.18);
    box-sizing: border-box;
  }
  .card-front { background: var(--card-white); }
  .card-back {
    background: linear-gradient(135deg, var(--card-navy) 0%, var(--card-navy-deep) 100%);
    display: flex;
    align-items: center;
    justify-content: center;
  }
  .identity {
    position: absolute;
    right: 370px;
    top: 150px;
    text-align: right;
    font-family: "Ubuntu", sans-serif;
  }
  .person-name {
    margin: 0;
    font-size: 26px;
    font-weight: 500;
    letter-spacing: 1.5px;
    color: var(--ink-navy);
  }
  .person-role {
    margin: 8px 0 0;
    font-size: 15px;
    letter-spacing: 1px;
    color: var(--ink-dark);
  }
  .divider {
    position: absolute;
    left: 345px;
    top: 145px;
    width: 2px;
    height: 150px;
    background: var(--rule);
  }
  .contact {
    position: absolute;
    left: 362px;
    top: 205px;
    margin: 0;
    padding: 0;
    list-style: none;
    font-family: "Ubuntu", sans-serif;
    font-size: 14px;
    line-height: 23px;
    letter-spacing: 0.8px;
    color: var(--ink-dark);
  }
  .contact-web {
    color: var(--ink-navy);
    font-weight: 500;
  }
  .brand-name {
    margin: 0;
    font-family: "Ubuntu", sans-serif;
    font-weight: 400;
    font-size: 34px;
    letter-spacing: 3px;
    color: var(--brand-light);
  }
</style>
</head>
<body>
  <main class="canvas">
    <section class="card card-front" aria-label="Business card, contact side">
      <div class="identity">
        <h1 class="person-name">ARLEN HALE</h1>
        <p class="person-role">MANAGING DIRECTOR</p>
      </div>
      <div class="divider"></div>
      <ul class="contact">
        <li>TEL: XXX XXX XXXX</li>
        <li>FAX: XXX XXX XXXX</li>
        <li>EMAIL: arlen@norvalecap.com</li>
        <li class="contact-web">www.norvalecap.com</li>
      </ul>
    </section>
    <section class="card card-back" aria-label="Business card, company side">
      <p class="brand-name">NORVALE CAPITAL</p>
    </section>
  </main>
</body>
</html>
```